Update Product Descriptions on Existing Website

We need to update product descriptions and images on three pages of our existing website. The tables are in editable HTML format. The formatting will be the exact same, just need the descriptions and images updated.

I have included the source documents below.

Coding

Coded - Design and coding required

Number of Pages Required

3 page

Colors

Designer to choose colors to be used in the design.

```html
<!DOCTYPE html>
<html lang="en">
<head>
<meta charset="utf-8">
<title>Molded Grating Sizes</title>
<link href="https://fonts.googleapis.com/css2?family=Montserrat:wght@600;700&family=Tinos&display=swap" rel="stylesheet">
<style>
  :root{
    --ink:#000;
    --paper:#fff;
    --link:#0000ee;
    --grating:#2e9a5c;
    --grating-light:#6cc48f;
    --frame:#c8c8c8;
  }
  html,body{margin:0;padding:0;width:1200px;height:661px;overflow:hidden;background:var(--paper);}
  .grating-table{
    position:absolute;left:283px;top:6px;width:624px;
    border-collapse:collapse;table-layout:fixed;
    font-family:"Tinos","Times New Roman",serif;font-size:9.4px;line-height:11px;color:var(--ink);
  }
  .grating-table td{border:1px solid var(--ink);padding:0 0 0 1px;vertical-align:middle;overflow:hidden;}
  .title-row td{
    height:18px;text-align:center;font-family:"Montserrat",sans-serif;font-weight:700;font-size:14px;line-height:18px;
  }
  .row{height:11.5px;}
  .row-tall{height:23px;}
  .image-row{height:81px;}
  .image-row td.cell{vertical-align:top;padding-top:1px;}
  .profile-label{vertical-align:middle;}
  .featured{text-align:center;vertical-align:top !important;padding-top:6px !important;}
  .featured .art{
    display:block;width:74px;height:46px;margin:0 auto;
    background:linear-gradient(135deg,var(--grating-light),var(--grating));border-radius:2px;
  }
  .featured .num{display:block;margin-top:13px;font-family:"Montserrat",sans-serif;font-weight:600;font-size:10px;}
  .empty-frame{display:block;width:77px;height:77px;border:1px solid var(--frame);box-sizing:border-box;}
  a{color:var(--link);}
</style>
</head>
<body>
<table class="grating-table">
  <colgroup>
    <col style="width:70px"><col style="width:109px"><col style="width:109px"><col style="width:109px"><col style="width:112.5px"><col style="width:114.5px">
  </colgroup>
  <tr class="title-row"><td colspan="6">The following sizes and types of molded grating are available from Norvale:</td></tr>

  <tr class="image-row">
    <td class="profile-label">Profile Image (click to enlarge)</td>
    <td class="featured"><span class="art" role="img" aria-label="Green molded grating profile, 2x2 mesh"></span><span class="num">1</span></td>
    <td class="featured"><span class="art" role="img" aria-label="Green molded grating profile, 1.5x1.5 mesh"></span><span class="num">2</span></td>
    <td class="featured"><span class="art" role="img" aria-label="Green molded grating profile, mini mesh"></span><span class="num">3</span></td>
    <td class="featured"><span class="art" role="img" aria-label="Green molded grating profile, 0.75 in high"></span><span class="num">4</span></td>
    <td class="featured"><span class="art" role="img" aria-label="Green molded grating profile, 1 in high"></span><span class="num">5</span></td>
  </tr>
  <tr class="row"><td>Height (in.)</td><td>0.5</td><td>0.5</td><td>0.5</td><td>0.75</td><td>1</td></tr>
  <tr class="row"><td>Mesh Size (in.)</td><td>2x2</td><td>1.5x1.5</td><td>.75x.75 1.5x1.5</td><td>1.5x1.5</td><td>1.5x1.5</td></tr>
  <tr class="row-tall"><td>Standard Panel Size(ft.)</td><td>4x12</td><td>12.4</td><td>12.5x4</td><td>12x4</td><td>10x4, 12x4</td></tr>
  <tr class="row"><td>Open Area</td><td>76%</td><td>72%</td><td>42%</td><td>69%</td><td>69%</td></tr>
  <tr class="row"><td>Weight (lbs./ft.)</td><td>1.2</td><td>1.33</td><td>2.15</td><td>1.88</td><td>2.52</td></tr>

  <tr class="row-tall">
    <td>Profile Image (click to enlarge)</td>
    <td><a href="#">Molded Grating 1in thick 1.5x1.5 mesh</a></td>
    <td><a href="#">Molded Grating 1in thick 1x4 mesh</a></td>
    <td><a href="#">Molded Grating 1in thick 1x4 mesh</a></td>
    <td><a href="#">Molded Grating 1in thick 0.75x0.75 mesh</a></td>
    <td><a href="#">Molded Grating 1.25in thick 1.5x1.5 mesh</a></td>
  </tr>
  <tr class="row"><td>Height (in.)</td><td>1</td><td>1</td><td>1</td><td>1</td><td>1.25</td></tr>
  <tr class="row"><td>Mesh Size (in.)</td><td>1.5x1.5</td><td>1x4</td><td>1x4</td><td>.75x.75 1.5x1.5</td><td>1.5x1.5</td></tr>
  <tr class="row-tall"><td>Standard Panel Size(ft.)</td><td>10x3, 13x3, 13x4</td><td>10x3 (bearing bars run width direction)</td><td>12x4 (bearing bars run width direction)</td><td>13x4, 8x4</td><td>12x4, 10x3, 13x5, 13x4</td></tr>
  <tr class="row"><td>Open Area</td><td>67%</td><td>67%</td><td>67%</td><td>38%</td><td>69%</td></tr>
  <tr class="row"><td>Weight (lbs./ft.)</td><td>2.5</td><td>2.83</td><td>2.68</td><td>3.17</td><td>2.99</td></tr>

  <tr class="image-row">
    <td class="profile-label">Profile Image (click to enlarge)</td>
    <td class="cell"><span class="empty-frame"></span></td><td class="cell"><span class="empty-frame"></span></td><td class="cell"><span class="empty-frame"></span></td><td class="cell"><span class="empty-frame"></span></td><td class="cell"><span class="empty-frame"></span></td>
  </tr>
  <tr class="row"><td>Height (in.)</td><td>1.25</td><td>1.25</td><td>1.25</td><td>1.5</td><td>1.5</td></tr>
  <tr class="row"><td>Mesh Size (in.)</td><td>1.5x1.5</td><td>.75x.75 1.5x1.5</td><td>.5x.5 1.5x1.5</td><td>1.5x1.5</td><td>6x1</td></tr>
  <tr class="row-tall"><td>Standard Panel Size(ft.)</td><td>10x3, 13x3, 13x4</td><td>13x3, 13x4</td><td>13x4</td><td>10x4, 12x4, 13x4, 13x5</td><td>12x4 (bearing bars run width direction)</td></tr>
  <tr class="row"><td>Open Area</td><td>67%</td><td>42%</td><td>30%</td><td>68%</td><td>56%</td></tr>
  <tr class="row"><td>Weight (lbs./ft.)</td><td>2.91</td><td>3.71</td><td>4.81</td><td>3.93</td><td>4.38</td></tr>

  <tr class="image-row">
    <td class="profile-label">Profile Image (click to enlarge)</td>
    <td class="cell"><span class="empty-frame"></span></td><td class="cell"><span class="empty-frame"></span></td><td class="cell"><span class="empty-frame"></span></td><td class="cell"><span class="empty-frame"></span></td><td class="cell"><span class="empty-frame"></span></td>
  </tr>
  <tr class="row"><td>Height (in.)</td><td>1.5</td><td>1.5</td><td>1.5</td><td>1.5</td><td>2</td></tr>
  <tr class="row"><td>Mesh Size (in.)</td><td>.75x.75 1.5x1.5</td><td>4x1.5</td><td>1.5x1.5</td><td>.75x.75 1.5x1.5</td><td>2x2</td></tr>
  <tr class="row-tall"><td>Standard Panel Size(ft.)</td><td>13x3, 13x4</td><td>12x4 (bearing bars run width direction)</td><td>10x3, 13x3, 13x4</td><td>13x4</td><td>12x4</td></tr>
  <tr class="row"><td>Open Area</td><td>42%</td><td>74%</td><td>67%</td><td>42%</td><td>69%</td></tr>
  <tr class="row"><td>Weight (lbs./ft.)</td><td>4.51</td><td>2.97</td><td>4.1</td><td>4.85</td><td>4.4</td></tr>

  <tr class="image-row">
    <td class="profile-label">Profile Image (click to enlarge)</td>
    <td class="cell"><span class="empty-frame"></span></td><td class="cell"><span class="empty-frame"></span></td><td class="cell"><span class="empty-frame"></span></td><td class="cell"><span class="empty-frame"></span></td><td class="cell"><span class="empty-frame"></span></td>
  </tr>
</table>
</body>
</html>
```